Banner Designs for Field Keep Ad Campaign

Harrowmere is a security consulting and services company that offers a service called FieldKeepUnit. FieldKeepUnit helps our customers secure large events by providing rapidly deployable security and communications technologies in a Field Keep vehicle, on a per event basis. We are looking for a designer to create a banner ad in three sizes for our campaign.
Target Market(s)
Our campaign is geared to the sports and entertainment industry, specifically large event venues and their security operation.
Industry/Entity Type
Security
Font styles to use
Other font styles liked:
- Raleway
Requirements
Must have
- Banner Objective
The visual and textual content of the banner should prompt the viewer to quickly identify the service offered and the information that is available to download.
Banner Design
Logo: FieldKeepUnit logo
Call to Action Button in Red: Get Details (On Right or or Upper Right)
Title in Larger Font: Take Control of you Events
Subtitle in smaller Font: Your Force Multiplier - Field Keep as a Service
Background: Photo of Field Keep interior or exterior or photo of female operator.
Font: Raleway
Banner Sizes
1 - 1200x670 pixels
2 - 1510x196 pixels
3 - 1200x628 pixels
Nice to have
- Follow the look and feel of the samples provided.

```html
<!DOCTYPE html>
<html lang="en">
<head>
<meta charset="utf-8">
<title>Field Keep Banner Set</title>
<link rel="stylesheet" href="https://fonts.googleapis.com/css2?family=Raleway:wght@500;600;700;800&display=swap">
<style>
  :root {
    --page: #ffffff;
    --navy: #0c1830;
    --navy-mid: #13284d;
    --stripe: #1c3868;
    --title-blue: #3b7cc9;
    --logo-blue: #4a86cf;
    --white: #ffffff;
    --ink: #0a0a0a;
    --photo-a: #1b3a66;
    --photo-b: #5f7fa8;
    --photo-c: #9fb2cc;
  }
  * { margin: 0; padding: 0; box-sizing: border-box; }
  html, body { width: 857px; height: 1200px; overflow: hidden; background: var(--page); }
  body { position: relative; font-family: "Raleway", sans-serif; }

  .banner {
    position: absolute;
    left: 78px;
    width: 710px;
    overflow: hidden;
    background: linear-gradient(115deg, var(--navy-mid) 0%, var(--navy) 45%, var(--navy) 100%);
    box-shadow: 10px 12px 18px rgba(0,0,0,0.45);
  }
  .banner--large { top: 51px; height: 394px; }
  .banner--strip { top: 539px; height: 121px; }
  .banner--medium { top: 755px; height: 371px; }

  .banner__backdrop { position: absolute; inset: 0; width: 100%; height: 100%; }

  .brand { position: absolute; color: var(--white); }
  .brand__name { display: block; font-weight: 600; color: var(--logo-blue); letter-spacing: 0.2px; }
  .brand__by { display: block; text-align: right; font-weight: 500; color: var(--white); }

  .headline { position: absolute; color: var(--title-blue); text-transform: uppercase; line-height: 0.95; }
  .headline__top { display: block; font-weight: 700; }
  .headline__bottom { display: block; font-weight: 800; }

  .tagline { position: absolute; color: var(--white); font-weight: 500; }

  .cta {
    position: absolute;
    background: var(--white);
    color: var(--ink);
    font-weight: 700;
    display: flex; align-items: center; justify-content: center;
  }

  /* large banner */
  .banner--large .brand { left: 20px; top: 20px; }
  .banner--large .brand__name { font-size: 25px; }
  .banner--large .brand__by { font-size: 11px; margin-top: 2px; }
  .banner--large .headline { left: 19px; top: 124px; }
  .banner--large .headline__top { font-size: 42px; }
  .banner--large .headline__bottom { font-size: 47px; letter-spacing: -0.5px; }
  .banner--large .tagline { left: 20px; top: 228px; font-size: 25px; line-height: 33px; }
  .banner--large .cta { left: 512px; top: 210px; width: 198px; height: 48px; font-size: 31px; border-radius: 24px 0 0 24px; }

  /* strip banner */
  .banner--strip .brand { left: 8px; top: 44px; }
  .banner--strip .brand__name { font-size: 14px; }
  .banner--strip .brand__by { font-size: 7px; }
  .banner--strip .headline { left: 170px; width: 230px; top: 14px; text-align: center; }
  .banner--strip .headline__top { font-size: 25px; }
  .banner--strip .headline__bottom { font-size: 28px; letter-spacing: -0.3px; }
  .banner--strip .tagline { left: 170px; width: 230px; top: 74px; font-size: 14px; line-height: 19px; text-align: center; }
  .cta-corner { position: absolute; right: 0; top: 0; width: 84px; height: 74px; }
  .cta-corner__label {
    position: absolute; right: 4px; top: 16px;
    font-size: 13px; font-weight: 600; color: var(--ink); text-align: center;
    line-height: 15px; transform: rotate(42deg);
  }

  /* medium banner */
  .banner--medium .brand { left: 20px; top: 20px; }
  .banner--medium .brand__name { font-size: 25px; }
  .banner--medium .brand__by { font-size: 11px; margin-top: 2px; }
  .banner--medium .headline { left: 15px; top: 111px; }
  .banner--medium .headline__top { font-size: 42px; }
  .banner--medium .headline__bottom { font-size: 47px; letter-spacing: -0.5px; }
  .banner--medium .tagline { left: 13px; top: 216px; font-size: 25px; line-height: 33px; }
  .banner--medium .cta { left: 495px; top: 219px; width: 208px; height: 48px; font-size: 31px; border-radius: 24px; }
</style>
</head>
<body>

<section class="banner banner--large">
  <svg class="banner__backdrop" viewBox="0 0 710 394" preserveAspectRatio="none">
    <defs>
      <linearGradient id="photoLarge" x1="0" y1="0" x2="1" y2="0.3">
        <stop offset="0" stop-color="#0c1830" stop-opacity="0"/>
        <stop offset="0.25" stop-color="#1b3a66"/>
        <stop offset="0.6" stop-color="#5f7fa8"/>
        <stop offset="1" stop-color="#9fb2cc"/>
      </linearGradient>
    </defs>
    <polygon points="60,0 180,0 0,260 0,150" fill="#1c3868" opacity="0.35"/>
    <polygon points="230,0 300,0 60,394 0,394" fill="#1c3868" opacity="0.25"/>
    <polygon points="400,0 440,0 180,394 140,394" fill="#1c3868" opacity="0.25"/>
    <g role="img" aria-label="Photo of a female operator with headset at a security control room desk">
      <polygon points="560,0 710,0 710,394 320,394 420,280" fill="url(#photoLarge)"/>
    </g>
  </svg>
  <div class="brand"><span class="brand__name">FieldKeepUnit</span><span class="brand__by">By Harrowmere</span></div>
  <h1 class="headline"><span class="headline__top">Take Control</span><span class="headline__bottom">Of You Events</span></h1>
  <p class="tagline">Your Force Multiplier -<br>Field Keep as a Service</p>
  <div class="cta">Get Details</div>
</section>

<section class="banner banner--strip">
  <svg class="banner__backdrop" viewBox="0 0 710 121" preserveAspectRatio="none">
    <defs>
      <linearGradient id="photoStrip" x1="0" y1="0" x2="1" y2="0">
        <stop offset="0" stop-color="#1b3a66"/>
        <stop offset="0.55" stop-color="#3e5f8f"/>
        <stop offset="1" stop-color="#7f97b9"/>
      </linearGradient>
    </defs>
    <polygon points="30,0 90,0 10,121 0,121 0,60" fill="#1c3868" opacity="0.35"/>
    <polygon points="170,0 200,0 120,121 90,121" fill="#1c3868" opacity="0.25"/>
    <polygon points="470,0 500,0 420,121 398,121" fill="#3b7cc9" opacity="0.8"/>
    <g role="img" aria-label="Photo of operators with headsets in front of control room monitors">
      <polygon points="485,0 710,0 710,121 430,121" fill="url(#photoStrip)"/>
    </g>
  </svg>
  <div class="brand"><span class="brand__name">FieldKeepUnit</span><span class="brand__by">By Harrowmere</span></div>
  <h2 class="headline"><span class="headline__top">Take Control</span><span class="headline__bottom">Of You Events</span></h2>
  <p class="tagline">Your Force Multiplier -<br>Field Keep as a Service</p>
  <svg class="cta-corner" viewBox="0 0 84 74"><polygon points="0,0 84,0 84,74" fill="#ffffff"/></svg>
  <div class="cta-corner__label">Get<br>Details</div>
</section>

<section class="banner banner--medium">
  <svg class="banner__backdrop" viewBox="0 0 710 371" preserveAspectRatio="none">
    <defs>
      <linearGradient id="photoMedium" x1="0" y1="0" x2="1" y2="0.3">
        <stop offset="0" stop-color="#0c1830" stop-opacity="0"/>
        <stop offset="0.25" stop-color="#1b3a66"/>
        <stop offset="0.6" stop-color="#5f7fa8"/>
        <stop offset="1" stop-color="#9fb2cc"/>
      </linearGradient>
    </defs>
    <polygon points="60,0 180,0 0,250 0,140" fill="#1c3868" opacity="0.35"/>
    <polygon points="230,0 300,0 70,371 0,371" fill="#1c3868" opacity="0.25"/>
    <polygon points="420,155 470,155 320,371 270,371" fill="#1c3868" opacity="0.35"/>
    <g role="img" aria-label="Photo of a female operator with headset at a security control room desk">
      <polygon points="560,0 710,0 710,371 320,371 420,260" fill="url(#photoMedium)"/>
    </g>
  </svg>
  <div class="brand"><span class="brand__name">FieldKeepUnit</span><span class="brand__by">By Harrowmere</span></div>
  <h2 class="headline"><span class="headline__top">Take Control</span><span class="headline__bottom">Of You Events</span></h2>
  <p class="tagline">Your Force Multiplier -<br>Field Keep as a Service</p>
  <div class="cta">Get Details</div>
</section>

</body>
</html>
```